Business Card for Polygraph business in Africa

Business Card . Polygraph Examiner based in Tanzania, East Africa.
Business Card will be used to disseminate contact information to potential clients.
It should convey that I am a professional specifically in the polygraph field and perform my work with integrity.

I have attached the business card that I'm currently using, which I threw together myself initially. It's not professional enough.

Target Market(s)

Banks, Accounting Firms, Government Ministries, Gas, Oil, & Gemstone Mining Concerns, Wildlife Conservation NGOs, International companies located in East Africa.

Industry/Entity Type

Business

Contact Information for Business Card

Veritas Lumeno
Harriet Munsell
PO Box 48317
Arusha, Tanzania
+255 712 839 254
harrietmunsell@quillpost.example

Colors
00a990
f37122
faa54b

Requirements
Must have
• - Veritas Lumeno (with the word "Polygraph" being more prominent than the word "Tanzania")
• - Forensic Examinations
• - Employment Screening
• - Should contain a logo of the Continental Truthfinder Guild (of which I'm a member)
• - I would like an accent design (such as the polygraph "squiggles" of a cardio tracing or such as that)
• - My contact information (less prominent, but large enough to read legibly). I would also consider putting the contact information on the second side of the card.
Nice to have
• My color suggestions are changeable.
Should not have
• Anything "cutesy" or "cartoonish"

```html
<!DOCTYPE html>
<html lang="en">
<head>
<meta charset="utf-8">
<title>Veritas Lumeno — Business Card</title>
<link href="https://fonts.googleapis.com/css2?family=Open+Sans:wght@400;600&display=swap" rel="stylesheet">
<style>
  :root {
    --backdrop: #3a3a3a;
    --card-dark: #141414;
    --card-light: #f2f2f2;
    --brand-grey: #8c8c8c;
    --ink: #7a7a7a;
    --ink-light: #ffffff;
    --teal: #00a990;
    --orange: #f37122;
    --badge: #d8d8d8;
  }
  * { margin: 0; padding: 0; box-sizing: border-box; }
  html, body {
    width: 1200px; height: 900px; overflow: hidden;
    background: var(--backdrop);
    font-family: "Open Sans", sans-serif;
  }
  .stage {
    width: 1200px; height: 900px;
    display: flex; align-items: center; justify-content: center; gap: 40px;
  }
  .card {
    position: relative;
    width: 540px; height: 310px;
    border-radius: 18px;
    overflow: hidden;
  }
  .card--front { background: var(--card-dark); }
  .card--back { background: var(--card-light); }

  .member-badge {
    position: absolute; top: 26px; right: 30px;
    width: 70px; height: 70px; border-radius: 50%;
    background: var(--badge);
  }
  .front-wordmark {
    position: absolute; top: 118px; left: 0; right: 0;
    text-align: center;
    font-size: 44px; font-weight: 600; letter-spacing: 0.5px;
    color: var(--brand-grey);
  }
  .services {
    position: absolute; bottom: 40px; left: 0; right: 0;
    text-align: center;
    font-size: 14px; color: var(--ink-light); letter-spacing: 0.3px;
  }
  .services .divider { margin: 0 14px; }

  .back-wordmark {
    position: absolute; left: 34px; top: 160px;
    font-size: 30px; font-weight: 600;
    color: var(--brand-grey);
  }
  .rule {
    position: absolute; left: 268px; top: 60px;
    width: 2px; height: 190px; background: var(--orange);
  }
  .contact {
    position: absolute; left: 292px; top: 66px; right: 20px;
    color: var(--ink);
  }
  .contact__name { font-size: 21px; margin-bottom: 16px; }
  .contact__row {
    display: flex; align-items: flex-start; gap: 10px;
    font-size: 13px; line-height: 1.4; margin-bottom: 10px;
  }
  .contact__row svg { flex: none; width: 14px; height: 14px; margin-top: 2px; fill: var(--teal); }
</style>
</head>
<body>
<main class="stage">
  <section class="card card--front">
    <div class="member-badge"></div>
    <div class="front-wordmark">Veritas Lumeno</div>
    <p class="services">Issue investigation<span class="divider">|</span>Employment screening</p>
  </section>

  <section class="card card--back">
    <div class="back-wordmark">Veritas Lumeno</div>
    <div class="rule"></div>
    <div class="contact">
      <p class="contact__name">Harriet Munsell</p>
      <div class="contact__row">
        <svg viewBox="0 0 24 24"><path d="M12 2a7 7 0 0 0-7 7c0 5 7 13 7 13s7-8 7-13a7 7 0 0 0-7-7zm0 9.5A2.5 2.5 0 1 1 12 6.5a2.5 2.5 0 0 1 0 5z"/></svg>
        <span>PO Box 48317<br>Arusha, Tanzania</span>
      </div>
      <div class="contact__row">
        <svg viewBox="0 0 24 24"><path d="M6.6 10.8a15 15 0 0 0 6.6 6.6l2.2-2.2a1 1 0 0 1 1-.25 11.4 11.4 0 0 0 3.6.57 1 1 0 0 1 1 1V20a1 1 0 0 1-1 1A17 17 0 0 1 3 4a1 1 0 0 1 1-1h3.5a1 1 0 0 1 1 1c0 1.25.2 2.45.57 3.57a1 1 0 0 1-.25 1z"/></svg>
        <span>+255 712 839 254</span>
      </div>
      <div class="contact__row">
        <svg viewBox="0 0 24 24"><path d="M2 5h20v14H2z M2 5l10 8 10-8" fill="none" stroke="#00a990" stroke-width="2"/></svg>
        <span>harrietmunsell@quillpost.example</span>
      </div>
    </div>
  </section>
</main>
</body>
</html>
```